Web Design Project

We have screen protector brand for mobile phone and we need
Looking for talented web designer. We need only graphic design of 3 page design Home, Catalog page and Product page

- Home page
- There will be rotating banners on the home page
- Top menu will have Hot products, Screen Protectors, Videos, Contact us
- Screen Protectors will be submenu
- Website will be two languages so put US and Turkish flags on the corner so users will be able to switch
- Home page, there will be newest products and hot products and also one video

I also live any additional creative idea for the website
There will be one inner page and catalog page

Check existing page www.vendrox.com which looks pretty bad. You can take logo from there. If you need logo separate i can send it.

I have attached the layout but feel free to change it. I only try to give idea what i wanna see on it.

```html
<!DOCTYPE html>
<html lang="en">
<head>
<meta charset="utf-8">
<title>Vendrox — Screen Protectors</title>
<link href="https://fonts.googleapis.com/css2?family=Open+Sans:ital,wght@0,300;0,400;0,600;0,700;1,400&family=Didact+Gothic&display=swap" rel="stylesheet">
<style>
:root{
  --orange:#f05a1e;
  --orange-dark:#d5470f;
  --topbar:#6a6a6a;
  --nav:#2b2b2b;
  --dropdown:#2a2a2a;
  --hero-top:#f2f2f2;
  --hero-bottom:#e9e9e9;
  --band:#e5e5e5;
  --page:#efefef;
  --text:#333;
  --muted:#7a7a7a;
  --footer:#262626;
  --footer-bottom:#0e0e0e;
  --field:#c9c9c9;
  --red:#e41e1e;
}
*{box-sizing:border-box;margin:0;padding:0}
html,body{width:963px;height:1200px;overflow:hidden}
body{position:relative;background:var(--page);font-family:"Open Sans",Arial,sans-serif;color:var(--text)}
.abs{position:absolute;white-space:nowrap}
p.abs{white-space:normal}

/* top bar */
.topbar{left:0;top:0;width:963px;height:38px;background:linear-gradient(#727272,#5f5f5f)}
.lang-label{left:672px;top:3px;font-size:11px;color:#fff}
.flag{top:3px;width:25px;height:16px;overflow:hidden}
.flag-us{left:763px}
.flag-tr{left:794px}

/* navigation */
.navbar{left:0;top:38px;width:963px;height:39px;background:repeating-linear-gradient(45deg,#2f2f2f 0 2px,#262626 2px 4px)}
.logo-tab{left:150px;top:30px;width:176px;height:72px}
.logo-name{left:150px;top:42px;width:176px;text-align:center;font-size:24px;font-weight:700;letter-spacing:1px;color:#3a3a3a}
.logo-name::before{content:"";display:inline-block;width:12px;height:12px;background:var(--orange);margin-right:7px;vertical-align:1px}
.nav-item{top:38px;height:39px;line-height:39px;font-size:14px;color:#fff;text-align:center}
.nav-active{left:519px;top:35px;width:123px;height:42px;background:linear-gradient(#f46a2a,#e04b12);line-height:44px}

/* dropdown */
.dropdown{left:412px;top:77px;width:408px;height:81px;background:var(--dropdown);border-top:3px solid var(--orange);z-index:5}
.dropdown ul{position:absolute;top:9px;list-style:none;font-size:11px;color:#e6e6e6;line-height:17px}

/* hero */
.hero{left:0;top:77px;width:963px;height:351px;background:linear-gradient(var(--hero-top),var(--hero-bottom))}
.slide-arrow{top:209px;width:46px;height:46px;border-radius:50%;background:#d6d6d6}
.phone-photo{left:276px;top:116px;width:141px;height:237px;border-radius:18px;background:linear-gradient(160deg,#3c3c3c,#111 60%,#cfd4d8)}
.hero-kicker{left:464px;top:128px;font-weight:300;font-size:43px;letter-spacing:6px;color:#4a4a4a;line-height:1}
.hero-title{left:464px;top:176px;font-size:29px;color:#3b3b3b;line-height:1}
.hero-text{left:472px;top:212px;width:240px;font-family:Arial,sans-serif;font-size:9.5px;line-height:13px;color:#666}
.btn-more{left:472px;top:266px;width:120px;height:35px;border-radius:4px;background:linear-gradient(#f7742f,#dc4710);box-shadow:0 2px 3px rgba(0,0,0,.25);color:#fff;font-size:12px;text-align:center;line-height:35px}
.slider-dots{left:449px;top:372px;width:65px;height:14px;border-radius:7px;background:#8a8a8a;display:flex;gap:3px;align-items:center;justify-content:center}
.slider-dots i{width:7px;height:7px;border-radius:50%;background:#444}
.slider-dots i.on{background:#d7e23b}

/* section tabs */
.section-tab{left:144px;width:188px;height:29px;background:#d3d3d3;clip-path:polygon(0 0,100% 0,92% 100%,8% 100%);font-family:"Didact Gothic",sans-serif;font-size:16px;color:#333;line-height:29px}

/* new products */
.products-band{left:0;top:428px;width:963px;height:244px;background:var(--band)}
.product{top:489px;width:115px;text-align:center}
.product-photo{height:103px;background:#fff;border:1px solid #cfcfcf;box-shadow:0 1px 2px rgba(0,0,0,.12);padding:8px 27px}
.product-photo div{height:100%;border-radius:5px;background:linear-gradient(135deg,#d9dde2,#8fa3bd 50%,#e3e6ea)}
.product-name{margin-top:13px;font-size:11px;line-height:16px;color:#333}
.product-price{font-size:11px;color:var(--orange);line-height:16px}

/* video */
.video-frame{left:143px;top:725px;width:341px;height:224px;background:linear-gradient(90deg,#3e3734,#6f6661 45%,#8a817d 60%,#3d3532)}
.divider{left:544px;top:710px;width:1px;height:262px;background:#dcdcdc}
.feature-icon{width:64px;height:64px;border-radius:50%;border:5px solid var(--red);background:#f4f4f4;left:594px}
.feature-title{left:671px;font-size:13px;font-weight:700;color:var(--orange)}
.feature-text{left:671px;width:135px;font-size:9px;line-height:13px;color:#777}

/* footer */
.footer{left:0;top:993px;width:963px;height:177px;background:var(--footer)}
.footer-bottom{left:0;top:1170px;width:963px;height:30px;background:var(--footer-bottom);text-align:center;font-size:9px;color:#8a8a8a;line-height:30px}
.footer-heading{font-size:14px;color:var(--orange)}
.quick-links{left:156px;top:1041px;list-style:none;font-family:Arial,sans-serif;font-style:italic;font-size:9.5px;line-height:17px;color:#fff}
.phone{left:352px;top:1043px;font-size:12px;color:#fff}
.address{left:352px;top:1058px;font-family:Arial,sans-serif;font-size:9.5px;line-height:11px;color:#777}
.social{top:1129px;width:21px;height:21px;border-radius:3px}
.field{background:var(--field);border:1px solid #e0e0e0;font-family:Arial,sans-serif;font-size:8.5px;color:#555;padding:6px 7px}
.btn{top:1131px;width:51px;height:21px;background:var(--orange);color:#fff;font-family:Arial,sans-serif;font-size:9px;font-weight:700;text-align:center;line-height:21px}
</style>
</head>
<body>

<div class="abs topbar"></div>
<div class="abs lang-label">Select Language:</div>
<svg class="abs flag flag-us" viewBox="0 0 25 16" role="img" aria-label="English">
  <rect width="25" height="16" fill="#fff"/>
  <g fill="#c8282e"><rect y="0" width="25" height="1.3"/><rect y="2.5" width="25" height="1.3"/><rect y="5" width="25" height="1.3"/><rect y="7.4" width="25" height="1.3"/><rect y="9.9" width="25" height="1.3"/><rect y="12.3" width="25" height="1.3"/><rect y="14.7" width="25" height="1.3"/></g>
  <rect width="11" height="8.7" fill="#2c3d7a"/>
</svg>
<svg class="abs flag flag-tr" viewBox="0 0 25 16" role="img" aria-label="Türkçe">
  <rect width="25" height="16" fill="#e30a17"/>
  <circle cx="9.5" cy="8" r="4.6" fill="#fff"/>
  <circle cx="10.7" cy="8" r="3.7" fill="#e30a17"/>
  <polygon points="15.2,8 17.6,7.2 17.6,5.8 18.3,7.2 20.2,7.4 18.5,8.4 19,10 17.6,8.9 16.1,9.8 16.9,8.2" fill="#fff"/>
</svg>

<div class="abs hero"></div>
<div class="abs navbar"></div>

<svg class="abs logo-tab" viewBox="0 0 176 72" aria-hidden="true">
  <polygon points="0,0 176,0 176,58 100,58 88,72 76,58 0,58" fill="#ececec"/>
  <polygon points="0,58 76,58 88,72 100,58 176,58 176,60 100,60 88,74 76,60 0,60" fill="#c7c7c7"/>
</svg>
<div class="abs logo-name">VENDROX</div>

<div class="abs nav-item" style="left:404px;width:94px">Hot Products</div>
<div class="abs nav-item nav-active">Screen Protectors</div>
<div class="abs nav-item" style="left:660px;width:56px">Videos</div>
<div class="abs nav-item" style="left:739px;width:80px">Contact Us</div>

<div class="abs slide-arrow" style="left:143px"><svg width="46" height="46"><polygon points="19,23 28,17 28,29" fill="#fff"/></svg></div>
<div class="abs slide-arrow" style="left:774px"><svg width="46" height="46"><polygon points="28,23 19,17 19,29" fill="#fff"/></svg></div>

<div class="abs phone-photo" role="img" aria-label="Smartphone with a clear screen protector film beside it"></div>

<div class="abs hero-kicker">WE PROVIDE</div>
<div class="abs hero-title">QUALITY PROTECTORS</div>
<p class="abs hero-text">Lorem Ipsum is simply dummy text of the printing and typesetting industry. Lorem Ipsum has been the industry's standard dummy text ever since the 1500s,</p>
<div class="abs btn-more">READ MORE</div>
<div class="abs slider-dots"><i class="on"></i><i></i><i></i><i></i></div>

<nav class="abs dropdown">
  <ul style="left:12px"><li>Lenza</li><li>Hextel</li><li>Sorrentel</li></ul>
  <ul style="left:116px"><li>Teklink</li><li>Movara</li><li>Solaro</li></ul>
  <ul style="left:221px"><li>Norvik</li><li>Kaori</li></ul>
  <ul style="left:325px"><li>Blackpine</li><li>Orchard</li></ul>
</nav>

<section class="abs products-band"></section>
<div class="abs section-tab" style="top:428px;padding-left:42px">New Products</div>

<div class="abs product" style="left:148px"><div class="product-photo" role="img" aria-label="Tablet with screen protector"><div></div></div><div class="product-name">Norvik<br>c7 Protector</div><div class="product-price">$45.00</div></div>
<div class="abs product" style="left:286px"><div class="product-photo" role="img" aria-label="Tablet with screen protector"><div></div></div><div class="product-name">Norvik<br>c7 Protector</div><div class="product-price">$45.00</div></div>
<div class="abs product" style="left:425px"><div class="product-photo" role="img" aria-label="Tablet with screen protector"><div></div></div><div class="product-name">Norvik<br>c7 Protector</div><div class="product-price">$45.00</div></div>
<div class="abs product" style="left:563px"><div class="product-photo" role="img" aria-label="Tablet with screen protector"><div></div></div><div class="product-name">Norvik<br>c7 Protector</div><div class="product-price">$45.00</div></div>
<div class="abs product" style="left:701px"><div class="product-photo" role="img" aria-label="Tablet with screen protector"><div></div></div><div class="product-name">Norvik<br>c7 Protector</div><div class="product-price">$45.00</div></div>

<div class="abs section-tab" style="top:672px;padding-left:78px">Video</div>

<div class="abs video-frame" role="img" aria-label="Video still of a product presentation at a trade show stand"></div>
<svg class="abs" style="left:284px;top:808px" width="58" height="58" aria-hidden="true">
  <circle cx="29" cy="29" r="28" fill="rgba(40,40,40,.75)"/>
  <polygon points="22,16 22,42 44,29" fill="#fff"/>
</svg>

<div class="abs divider"></div>

<div class="abs feature-icon" style="top:719px" role="img" aria-label="No-scratch symbol"></div>
<div class="abs feature-title" style="top:735px">Anti Scratch</div>
<p class="abs feature-text" style="top:752px">See the app live in action on some of the latest phones.</p>

<div class="abs feature-icon" style="top:806px" role="img" aria-label="No-fingerprint symbol"></div>
<div class="abs feature-title" style="top:816px">Anti FingerPrint</div>
<p class="abs feature-text" style="top:833px">Try before you buy. Download the latest free trial version.</p>

<div class="abs feature-icon" style="top:890px;background:#fff" aria-hidden="true">
  <svg width="54" height="54" viewBox="0 0 54 54"><polyline points="12,27 23,38 42,14" fill="none" stroke="#e41e1e" stroke-width="7"/></svg>
</div>
<div class="abs feature-title" style="top:901px">Washable</div>
<p class="abs feature-text" style="top:917px">Need help? found a bug? we can help. Free Tech Support.</p>

<footer>
  <div class="abs footer"></div>
  <div class="abs footer-heading" style="left:155px;top:1014px">Quick Links</div>
  <ul class="abs quick-links">
    <li>Home</li><li>Products</li><li>Hot products</li><li>Screen Protectors</li><li>Videos</li><li>Contact Us</li>
  </ul>

  <div class="abs footer-heading" style="left:352px;top:1014px">Contact Us</div>
  <div class="abs phone">(555) 203-4718</div>
  <p class="abs address">118 N. Alder St<br>PO Box 512<br>Riverton, Iowa 11111</p>
  <div class="abs footer-heading" style="left:350px;top:1099px">Follow Us</div>
  <div class="abs social" style="left:352px;background:#3b5a9a"></div>
  <div class="abs social" style="left:378px;background:#4fb6d8"></div>
  <div class="abs social" style="left:403px;background:#f08a24"></div>

  <div class="abs footer-heading" style="left:556px;top:1014px">Quick Contact</div>
  <div class="abs field" style="left:557px;top:1037px;width:126px;height:21px">Type Your Name</div>
  <div class="abs field" style="left:692px;top:1037px;width:126px;height:21px">Type Your Email</div>
  <div class="abs field" style="left:557px;top:1064px;width:261px;height:61px">Type Your Message</div>
  <div class="abs btn" style="left:709px">Reset</div>
  <div class="abs btn" style="left:767px">Send</div>

  <div class="abs footer-bottom">© Copyright 2012, vendrox.com</div>
</footer>

</body>
</html>
```